Wordpress Design Project

We need a wordpress design for a new creative innovation company based in Melbourne called BoldMosaiqua.
We develop innovative growth and communication strategies for our clients who are generally medium sized businesses wanting to find new ways to grow their businesses.
Our Services include:
Business Strategy
Communications and Strategic Planning
Creative Consultancy
Professional Development
Change Management
Project Management
We would like our wordpress design to be simple and professional yet give a feeling of innovation, kind of like old meeting new.
We are leaning towards the predominant background colour being white, but open to suggestions.
Attached are logo files.
If you require any further information please contact us via the Sketch Hive site.

```html
<!DOCTYPE html>
<html lang="en">
<head>
<meta charset="utf-8">
<title>BoldMosaiqua</title>
<link href="https://fonts.googleapis.com/css2?family=Source+Sans+3:wght@400;600&family=Roboto+Condensed:wght@400&family=Open+Sans:wght@400&family=Arimo:wght@400&display=swap" rel="stylesheet">
<style>
:root{
  --green:#8cc63e;
  --green-dark:#5aa22f;
  --green-text:#5ea32f;
  --menu-green:#5ea832;
  --text:#555a5f;
  --top-bar:#5a6470;
  --line:#d9d9d9;
  --footer:#efefef;
}
*{margin:0;padding:0;box-sizing:border-box}
html,body{width:1119px;height:1200px;overflow:hidden;background:#fff}
body{position:relative;font-family:"Source Sans 3",sans-serif;color:var(--text)}
.abs{position:absolute}
.top-bar{left:0;top:0;width:1119px;height:12px;background:var(--top-bar)}
.header-band{left:0;top:143px;width:1119px;height:320px;background:linear-gradient(#f5f5f5,#fbfbfb 60%,#fff)}
.logo{left:93px;top:44px;font-size:46px;font-weight:400;color:var(--green);letter-spacing:-1px}
.social{top:66px;width:24px;height:24px;border-radius:50%;background:var(--green)}
.nav{left:93px;top:125px;width:934px;height:36px;border-radius:12px 12px 0 0;background:linear-gradient(#a2e06e,#6cc23a 55%,#5aae2e);font-family:"Arimo",sans-serif;font-size:13px;color:#1d2a12}
.nav a{position:absolute;top:0;height:36px;line-height:38px;text-align:center;color:inherit;text-decoration:none;border-right:1px solid rgba(255,255,255,.35)}
.nav .home{left:0;width:59px;background:linear-gradient(#6cbf3a,#3f8c22);border-radius:12px 0 0 0}
.nav .active{background:linear-gradient(#6cb73f,#5ba132)}
.search{left:825px;top:132px;width:185px;height:23px;border-radius:12px;background:#fff;border:1px solid #6aa540;box-shadow:inset 0 1px 2px rgba(0,0,0,.2)}
.hero{left:93px;top:160px;width:934px;height:278px;background:linear-gradient(90deg,#cfdde8 0%,#e9f1f6 40%,#d8e8f1 65%,#f4f8fa 100%);border:1px solid #c9cfd4}
.hero-shadow{left:70px;top:436px;width:980px;height:14px;background:radial-gradient(ellipse at top,rgba(0,0,0,.35),rgba(0,0,0,0) 70%)}
.dropdown{left:247px;top:160px;width:266px;height:174px;background:var(--menu-green);border:1px solid #4e8f29;list-style:none;padding:12px 0 0 20px;font-family:"Arimo",sans-serif;font-size:11px;color:#fff}
.dropdown li{height:25.3px}
.dropdown li::before{content:"•";margin-right:7px}
.caption{left:684px;top:340px;font-family:"Open Sans",sans-serif;color:#3d4246}
.caption .l1{font-size:20px}
.caption .l2{font-size:30px;margin-top:4px}
.dots{left:467px;top:404px;width:204px;height:34px}
h1.welcome{left:94px;top:478px;font-size:26px;font-weight:400;color:var(--green)}
.intro{left:94px;top:521px;width:656px;font-size:12.3px;line-height:21.4px;text-align:justify}
.photo{border:3px solid #e3e6e8;border-radius:4px;background:linear-gradient(135deg,#dfe6ec,#c4cfd8 50%,#eef0f2)}
.rule{height:1px;background:var(--line)}
.vrule{width:1px;background:var(--line)}
.col{top:672px;width:282px}
.col h2{font-family:"Roboto Condensed",sans-serif;font-weight:400;font-size:22px;color:var(--green-text);height:42px;display:flex;align-items:center;gap:7px}
.col p{font-size:12.3px;line-height:21.4px;text-align:justify;margin-top:4px}
.more{font-size:12px;color:var(--green-text);text-transform:uppercase}
.more::after{content:"";display:inline-block;margin-left:8px;border-left:5px solid var(--green-text);border-top:4px solid transparent;border-bottom:4px solid transparent}
h2.section{font-family:"Roboto Condensed",sans-serif;font-weight:400;font-size:22px;color:var(--green-text)}
.blog-text{left:281px;top:935px;width:419px;font-size:12.3px;line-height:21.4px;text-align:justify}
.blog-text p+p{margin-top:8px}
.news{left:744px;top:935px;width:283px;list-style:none;font-size:12.3px;line-height:19.5px}
.news li{position:relative;padding-left:25px;height:53px;text-align:justify}
.news li::before{content:"";position:absolute;left:4px;top:6px;border-left:6px solid var(--green-text);border-top:4px solid transparent;border-bottom:4px solid transparent}
.footer{left:0;top:1156px;width:1119px;height:44px;background:var(--footer);text-align:center;line-height:44px;font-size:12px;color:#666}
</style>
</head>
<body>
<div class="abs top-bar"></div>
<div class="abs header-band"></div>

<div class="abs logo">BoldMosaiqua</div>
<span class="abs social" style="left:907px"></span>
<span class="abs social" style="left:940px"></span>
<span class="abs social" style="left:973px"></span>
<svg class="abs" style="left:1005px;top:66px" width="24" height="24" viewBox="0 0 24 24"><circle cx="12" cy="12" r="12" fill="#8cc63e"/><rect x="6" y="8" width="12" height="8.5" fill="none" stroke="#fff" stroke-width="1.4"/><path d="M6 8l6 5 6-5" fill="none" stroke="#fff" stroke-width="1.4"/></svg>

<nav class="abs nav">
  <a class="home" href="#" style="left:0"><svg width="16" height="14" viewBox="0 0 16 14" style="margin-top:11px"><path d="M8 0L0 7h2v7h4.5v-4h3v4H14V7h2z" fill="#fff"/></svg></a>
  <a href="#" style="left:59px;width:95px">About us</a>
  <a class="active" href="#" style="left:154px;width:91px">Services</a>
  <a href="#" style="left:245px;width:113px">Testimonials</a>
  <a href="#" style="left:358px;width:74px">Blogs</a>
  <a href="#" style="left:432px;width:103px">Contact us</a>
</nav>
<div class="abs search"><svg style="position:absolute;right:6px;top:4px" width="14" height="14" viewBox="0 0 14 14"><circle cx="5.5" cy="5.5" r="4.3" fill="none" stroke="#555" stroke-width="1.4"/><path d="M8.7 8.7l4.3 4.3" stroke="#555" stroke-width="1.8"/></svg></div>

<div class="abs hero" role="img" aria-label="Businesswoman in a dark suit beside a hand touching glowing interface tiles"></div>
<div class="abs hero-shadow"></div>
<ul class="abs dropdown">
  <li>Business Strategy</li>
  <li>Communications and Strategic Planning</li>
  <li>Creative Consultancy</li>
  <li>Professional Development</li>
  <li>Change Management</li>
  <li>Project Management</li>
</ul>
<div class="abs caption"><div class="l1">Vivamus feugiat egestas lacus,</div><div class="l2">vitae pulvinar tellus</div></div>
<svg class="abs dots" viewBox="0 0 204 34"><path d="M0 34C14 34 20 4 40 4H165C184 4 190 34 204 34Z" fill="#3a3d40"/><circle cx="62" cy="19" r="6" fill="#fff"/><circle cx="88" cy="19" r="6" fill="#1c1e20"/><circle cx="114" cy="19" r="6" fill="#1c1e20"/><circle cx="138" cy="19" r="6" fill="#1c1e20"/></svg>

<h1 class="abs welcome">Welcome to our site</h1>
<p class="abs intro">Sed ut perspiciatis unde omnis iste natus error sit voluptatem accusantium doloremque laudantium, totam rem aperiam, eaque ipsa quae ab illo inventore veritatis et quasi architecto beatae vitae dicta sunt explicabo. Nemo enim ipsam voluptatem quia voluptas sit aspernatur aut odit aut fugit, sed quia consequuntur magni dolores eos qui ratione voluptatem sequi nesciunt. Neque porro quisquam est, qui dolorem ipsum quia dolor sit amet, consectetur, adipisci velit, sed quia non numquam eius modi tempora incidunt ut labore et dolore magnam aliquam quaerat.</p>
<div class="abs photo" style="left:767px;top:484px;width:255px;height:135px" role="img" aria-label="Smiling team celebrating in an office"></div>

<div class="abs rule" style="left:93px;top:652px;width:934px"></div>

<section class="abs col" style="left:94px">
  <h2><svg width="30" height="40" viewBox="0 0 30 40"><circle cx="15" cy="10" r="7" fill="#6b7480"/><path d="M2 40V28c0-6 6-9 13-9s13 3 13 9v12z" fill="#3c4550"/><path d="M13 20h4l-1 14h-2z" fill="#fff"/></svg>ABOUT US</h2>
  <p>Nemo enim ipsam voluptatem quia voluptas sit aspernatur aut odit aut fugit, sed quia consequuntur magni dolores eos qui ratione voluptatem sequi nesciunt. Neque porro quisquam est.</p>
  <div class="more" style="margin-top:12px">View more</div>
</section>
<div class="abs vrule" style="left:397px;top:672px;height:163px"></div>
<section class="abs col" style="left:420px">
  <h2><svg width="38" height="38" viewBox="0 0 38 38"><circle cx="19" cy="19" r="15" fill="none" stroke="#7d8791" stroke-width="6" stroke-dasharray="5 3.2"/><circle cx="19" cy="19" r="12" fill="#8a949e"/><circle cx="19" cy="19" r="8" fill="#1d6fc0"/><circle cx="19" cy="19" r="4" fill="#fff"/></svg>OUR SERVICES</h2>
  <p>Nemo enim ipsam voluptatem quia voluptas sit aspernatur aut odit aut fugit, sed quia consequuntur magni dolores eos qui ratione voluptatem sequi nesciunt. Neque porro quisquam est.</p>
  <div class="more" style="margin-top:12px">View more</div>
</section>
<div class="abs vrule" style="left:723px;top:672px;height:163px"></div>
<section class="abs col" style="left:745px">
  <h2><svg width="34" height="30" viewBox="0 0 34 30"><path d="M17 3C8 3 2 8 2 14c0 4 2 7 6 9l-2 6 7-4c1 0 3 .5 4 .5 9 0 15-5 15-11.5S26 3 17 3z" fill="#c9ced3"/><text x="10" y="18" font-size="12" fill="#555" font-family="serif">“ ”</text></svg>TESTIMONIALS</h2>
  <p><span style="font-family:serif;font-size:18px;font-weight:bold;color:#777;margin-right:8px">“</span>Nemo ipsam voluptatem quia voluptas sit aspernatur aut odit aut fugit, sed quia consequuntur magni dolores eos qui ratione voluptatem sequi nesciunt. Neque porro quisquam est. <span style="font-family:serif;font-size:18px;font-weight:bold;color:#777;margin-left:6px">”</span></p>
  <div class="more" style="margin-top:10px">View more</div>
</section>

<div class="abs rule" style="left:93px;top:867px;width:934px"></div>

<h2 class="abs section" style="left:94px;top:890px">BLOG</h2>
<div class="abs photo" style="left:94px;top:939px;width:164px;height:191px" role="img" aria-label="Excited man cheering behind a laptop"></div>
<div class="abs blog-text">
  <p>Sed ut perspiciatis unde omnis iste natus error sit voluptatem accusantium doloremque laudantium, totam rem aperiam, eaque ipsa quae ab illo inventore veritatis et quasi architecto beatae vitae dicta sunt explicabo. Nemo enim ipsam voluptatem quia voluptas sit aspernatur aut odit aut fugit, sed quia consequuntur magni dolores eos qui ratione voluptatem sequi nesciunt.</p>
  <p>At vero eos et accusamus et iusto odio dignissimos ducimus qui blanditiis praesentium voluptatum deleniti atque corrupti quos dolores.</p>
</div>
<div class="abs more" style="left:282px;top:1106px">View more</div>

<div class="abs vrule" style="left:723px;top:939px;height:192px"></div>
<h2 class="abs section" style="left:744px;top:888px">LATEST NEWS</h2>
<ul class="abs news">
  <li>Atveroeos accusamus et iusto odio dignissi mos ducimus blanditiis praesentium.</li>
  <li>Atveroeos accusamus et iusto odio dignissi mos ducimus blanditiis praesentium.</li>
  <li>Atveroeos accusamus et iusto odio dignissi mos ducimus blanditiis praesentium.</li>
  <li>Atveroeos accusamus et iusto odio dignissi mos ducimus blanditiis praesentium.</li>
</ul>

<footer class="abs footer">Copyright © 2012 BoldMosaiqua. All rights reserved.</footer>
</body>
</html>
```